Corporate Reception Invite (Thursday Gather: CorkPop Series)

I am looking for an invitation to use in Constant Contact for an upcoming reception. I have attached the company logo and a hero image from the reception location that may work well. Lastly, I attached an example from last year's invite for reference. Event details:

Thursday Gather: CorkPop Series @ QRB
October 23rd, 2023 from 6:00 - 8:00 pm
Marcella at The Halvorsen, Chicago
418 N Pellham Ave, Chicago, IL 60699
Join RBK & Friends for Cocktails & Conversation
Super casual - come and go as you please. Guests welcome.

Target Market(s)

Corporate audience

Font styles to use
Serif
Script
Other font styles liked:
• No strong preference, but want something elegant, sexy, and corporate

Colors
0054AA
0677BA
7BADD7
CADEEF
E8F1F8

Requirements
Must have
• RBK logo, event details, size: 600 x 1500 pixels

```html
<!DOCTYPE html>
<html lang="en">
<head>
<meta charset="utf-8">
<title>Thursday Gather: CorkPop Series @ QRB</title>
<link rel="stylesheet" href="https://fonts.googleapis.com/css2?family=EB+Garamond:wght@400;600&family=Allura&display=swap">
<style>
  :root {
    --page-bg: #f2f2f2;
    --navy: #0a2d8a;
    --brand-blue: #0677ba;
    --mid-blue: #0054aa;
    --sky: #7badd7;
    --mist: #cadeef;
    --ice: #e8f1f8;
    --white: #ffffff;
    --script-blue: #6fb4e6;
    --hero-top: #9aa3ad;
    --hero-bottom: #4a4540;
  }
  * { box-sizing: border-box; margin: 0; padding: 0; }
  html, body {
    width: 1200px; height: 1200px; overflow: hidden;
    background: var(--page-bg);
  }
  .invite {
    position: absolute; left: 380px; top: 50px;
    width: 440px; height: 1100px;
    background: var(--navy);
    overflow: hidden;
  }
  .hero-photo {
    position: absolute; left: 0; top: 0; width: 440px; height: 460px;
    background: linear-gradient(180deg, var(--hero-top) 0%, var(--hero-bottom) 100%);
  }
  .waves { position: absolute; left: 0; top: 0; width: 440px; height: 1100px; }
  .details {
    position: absolute; left: 0; top: 536px; width: 440px;
    text-align: center; color: var(--white);
    font-family: "EB Garamond", Georgia, serif;
  }
  .event-title {
    font-weight: 600; font-size: 34px; line-height: 40px;
  }
  .event-date {
    margin-top: 21px; font-size: 18px; line-height: 24px;
    display: flex; justify-content: center; align-items: center; gap: 14px;
  }
  .event-date .dot {
    width: 5px; height: 5px; border-radius: 50%; background: var(--white);
  }
  .event-venue { margin-top: 15px; font-size: 18px; line-height: 24px; }
  .invite-line {
    margin-top: 13px; font-family: "Allura", cursive;
    font-size: 37px; line-height: 34px; color: var(--script-blue);
  }
  .event-note { margin-top: 9px; font-size: 18px; line-height: 24px; }
  .brand-badge {
    position: absolute; left: 149px; top: 890px;
    width: 145px; height: 98px; border-radius: 14px;
    background: var(--white);
    display: flex; align-items: center; justify-content: center; gap: 10px;
    z-index: 2;
  }
  .brand-badge .mark { width: 16px; height: 16px; background: var(--brand-blue); }
  .brand-badge .name {
    font-family: "EB Garamond", Georgia, serif; font-weight: 600;
    font-size: 34px; color: var(--navy);
  }
</style>
</head>
<body>
  <main class="invite">
    <div class="hero-photo" role="img" aria-label="Photo of wine glasses at the reception venue"></div>

    <svg class="waves" viewBox="0 0 440 1100" aria-hidden="true">
      <defs>
        <linearGradient id="topBand" x1="0" y1="0" x2="1" y2="0">
          <stop offset="0" stop-color="#7aa2e0"/>
          <stop offset=".35" stop-color="#6fb0e6"/>
          <stop offset=".7" stop-color="#4a86da"/>
          <stop offset="1" stop-color="#0677ba"/>
        </linearGradient>
        <linearGradient id="bottomBand" x1="0" y1="0" x2="1" y2="0">
          <stop offset="0" stop-color="#4a5eb0"/>
          <stop offset="1" stop-color="#2a3f9c"/>
        </linearGradient>
        <linearGradient id="footer" x1="0" y1="0" x2="1" y2="0">
          <stop offset="0" stop-color="#4a78c8"/>
          <stop offset=".6" stop-color="#3a55aa"/>
          <stop offset="1" stop-color="#1a3590"/>
        </linearGradient>
      </defs>
      <path d="M0 423 C80 440 160 455 230 448 C320 440 390 410 440 386 L440 1100 L0 1100 Z" fill="url(#topBand)"/>
      <path d="M0 441 C90 470 170 510 250 507 C340 503 400 478 440 460 L440 1100 L0 1100 Z" fill="var(--white)"/>
      <path d="M0 446 C90 476 170 516 250 513 C340 509 400 484 440 468 L440 1100 L0 1100 Z" fill="var(--navy)"/>
      <path d="M0 945 C60 990 160 1040 280 1040 C360 1040 410 1020 440 1000 L440 1100 L0 1100 Z" fill="url(#bottomBand)"/>
      <path d="M0 1058 C120 1066 260 1074 340 1058 C390 1048 420 1030 440 1012 L440 1100 L0 1100 Z" fill="var(--white)"/>
      <path d="M0 1061 C120 1069 260 1077 340 1062 C390 1052 420 1034 440 1018 L440 1100 L0 1100 Z" fill="url(#footer)"/>
    </svg>

    <section class="details">
      <h1 class="event-title">Thursday Gather:<br>CorkPop Series @ QRB</h1>
      <p class="event-date"><span class="dot"></span>October 23rd, 2023 from 6:00 - 8:00 pm<span class="dot"></span></p>
      <p class="event-venue">Marcella at The Halvorsen, Chicago<br>418 N Pellham Ave, Chicago, IL 60699</p>
      <p class="invite-line">Join RBK &amp; Friends<br>for Cocktails &amp; Conversation</p>
      <p class="event-note">Super casual - come and go as you please. Guests welcome.</p>
    </section>

    <div class="brand-badge">
      <span class="mark"></span>
      <span class="name">RBK</span>
    </div>
  </main>
</body>
</html>
```